依頼詳細
【用途】売家・売地などに使用
【重視】シンプル&インパクト(目を引く・意外性)
記載項目
ロゴ、社名、電話、QRコード
希望イメージ
シンプル 複雑
単色 カラフル
暗い 明るい
日常 高級
遊び心 厳粛
未来的 伝統的
女性的 男性的
希望する色
青系、水色系、ロゴのポイントカラーは水色、その他はお任せします
納品ファイル
• 高解像度JPG (.jpg)
• イラストレーター形式 (.ai)
• フォトショップ形式 (.psd)
補足説明
のぼりへの表記文字は「売物件」としてください。
GW期間中の為期間を延長し、報酬も少し上げたいと思います。
データの支給の要望がありましたので添付します。のぼり既製品よりいいデザインを期待しておりますので、よろしくお願いします。
応募数がある程度集まってきましたので、申し訳ありませんが納期を短くします。
■ 選んだ理由

インパクトの面でfukuzono-studio様のデザインを選定。独創性の面でTRnoki様のデザインを選定させていただきました。双方とも他にはない特徴がありこちらの意図を汲みとってもらえました。ありがとうございました。

■ 提案者全員のお礼・コメント

いつもながらに素晴らしいデザインが多々あり選定に相当悩みましたが、最終的には4迄絞りからどうしても外せない2案を当選とさせて頂きました。クリエタの皆様の質の高さにいつもながらに驚かされます。ありがとうございました。感謝!

```html
<!DOCTYPE html>
<html lang="ja">
<head>
<meta charset="utf-8">
<title>売物件 のぼり</title>
<link href="https://fonts.googleapis.com/css2?family=Noto+Sans+JP:wght@500;700;900&display=swap" rel="stylesheet">
<style>
  :root {
    --blue: #2f86c4;
    --navy: #2b2f3a;
    --white: #ffffff;
    --pole: #9a9ea6;
    --page: #ffffff;
  }
  * { margin: 0; padding: 0; box-sizing: border-box; }
  html, body { width: 846px; height: 1200px; overflow: hidden; background: var(--page); }
  body { position: relative; font-family: "Noto Sans JP", sans-serif; }

  .pole-loops { position: absolute; left: 0; top: 0; }

  .banner {
    position: absolute; left: 220px; top: 164px;
    width: 406px; height: 885px;
    background: var(--white);
    border: 2px solid #d5d7db;
    overflow: hidden;
  }
  .side-stripe {
    position: absolute; left: 372px; top: 30px;
    width: 22px; height: 690px; background: var(--blue);
  }
  .title-disc {
    position: absolute; left: 24px; top: 120px;
    width: 176px; height: 176px; border-radius: 50%;
    background: var(--navy);
  }
  .title-char {
    position: absolute; font-weight: 900; line-height: 1;
  }
  .char-uri   { left: 24px; top: 120px; width: 176px; text-align: center; font-size: 160px; line-height: 176px; color: var(--blue); }
  .char-butsu { left: 30px; top: 300px; font-size: 196px; color: var(--navy); }
  .char-ken   { left: 30px; top: 505px; font-size: 196px; color: var(--navy); }

  .reading {
    position: absolute; left: 312px; top: 330px;
    writing-mode: vertical-rl; font-size: 40px; font-weight: 700;
    color: var(--blue); letter-spacing: 2px;
  }

  .company {
    position: absolute; left: 22px; top: 735px;
    display: flex; align-items: center; gap: 12px;
  }
  .company-dot { width: 40px; height: 40px; border-radius: 50%; background: var(--navy); }
  .company-name { font-size: 34px; font-weight: 700; color: var(--navy); }

  .contact-band {
    position: absolute; left: 0; bottom: 0; width: 100%; height: 92px;
    background: var(--blue); color: var(--white);
    display: flex; align-items: center; padding-left: 18px;
  }
  .phone-icon { width: 54px; height: 54px; flex: none; }
  .phone-prefix {
    margin-left: 10px; font-size: 24px; font-weight: 700; line-height: 1.05;
  }
  .phone-main {
    margin-left: 10px; font-size: 74px; font-weight: 900; line-height: 1; letter-spacing: 1px;
  }
</style>
</head>
<body>
  <svg class="pole-loops" width="846" height="1200" aria-hidden="true">
    <g fill="none" stroke="var(--pole)" stroke-width="3">
      <line x1="160" y1="166" x2="626" y2="166"/>
      <rect x="160" y="350" width="60" height="22"/>
      <rect x="160" y="550" width="60" height="22"/>
      <rect x="160" y="750" width="60" height="22"/>
      <rect x="160" y="950" width="60" height="22"/>
    </g>
  </svg>

  <section class="banner">
    <div class="side-stripe"></div>

    <div class="title-disc"></div>
    <div class="title-char char-uri">売</div>
    <div class="title-char char-butsu">物</div>
    <div class="title-char char-ken">件</div>

    <div class="reading">うりぶっけん</div>

    <div class="company">
      <span class="company-dot"></span>
      <span class="company-name">ミナト不動産</span>
    </div>

    <div class="contact-band">
      <svg class="phone-icon" viewBox="0 0 54 54" aria-label="電話">
        <circle cx="27" cy="27" r="25" fill="var(--white)"/>
        <path d="M19 14c2 0 3 1 4 4l1 4c0 2-2 3-3 4 2 4 4 6 8 8 1-1 2-3 4-3l4 1c3 1 4 2 4 4 0 3-3 5-6 5-11 0-20-9-20-20 0-3 2-7 4-7z" fill="var(--blue)"/>
      </svg>
      <div class="phone-prefix">(098)<br>555-</div>
      <div class="phone-main">0172</div>
    </div>
  </section>
</body>
</html>
```